NOTE: I PROVIDED THE INCORRECT LOGO AND ONLY A HANDFUL OF PEOPLE NOTICED THAT IT WAS NOT THE ONE I DESCRIBED. THE LOGO I HAVE NOW ATTACHED MATCHES MY WEBSITE AND THE COLORS ON THE WEBSITE SHOULD BE USED FOR THE CARD.

PLEASE READ THE BUSINESS CARD DETAILS AND PROJECT MUST HAVES CAREFULLY.

I am looking for a business card that is powerful, a bit edgy, and although I work in the corporate world, not too formal. I would like to see designs that use the colors on my website www.brightmoorlane.com. I don't want the card to look washed out so please use shades of those colors that make them "pop". The "vibe" of the card needs to show substance and confidence while also reflecting that we're not your usual consultants.

The focus of my work is turning "people problems" into profits. Those problems could be poor service, an unstable workforce, untrained leaders, or managing change. We are an aggressive, results-focused team of performance improvement professionals who refuse to believe "things can't be done". For us, failure is not an option. Our logo reflects a target from the view of the site on a gun.

In addition to the contact information provided on the sample business card (do not include "turning people problems into profits"), I would like to include this statement (probably on the back):
I equip results-oriented business leaders to turn their people problems into profits in six months or less.

PLEASE NOTE THAT MY WEBSITE IS UNDER REVISION TO TONE DOWN THE MILITARY THEME, ALTHOUGH THE WARRIOR ENERGY AND FOCUS ON RESULTS REMAINS.

Target Market(s)

My clients are Mid and senior-level managers. I don't target any particular industry.

Industry/Entity Type

Consulting

Contact Information for Business Card

In addition to the contact information provided on the sample business card (DO NOT INCLUDE "turning people problems into profits"), I would like to include this statement (probably on the back):

I don't care whether the card is landscape or portrait view.

Font styles to use
Sans Serif

Requirements
Must have
• 1. be easy to read, no 6-8 point fonts!
• 2. a "vibe" that captures the eye without being too chaotic or busy
• 3. bold color, not washed out or boring - a good blend with the colors currently on my website (black, red, white, army green) but you don't need to use all of them.
• 4. all the contact information I have provided
• 5. a good blend with the colors currently on my website
• 6. Must have this quote on the back of the card: I equip results-oriented business leaders to turn their people problems into profits in six months or less.
Nice to have
• In looking at the sample images I provided for ideas, you can see that I like the way a card carries over from one side to the next.
• It would be great to find some aspect/quality/feature that I haven't seen before
Should not have
• 1. NO use of ALL CAPS
• 2. fonts that I would have to seek out and purchase (you should provide files for font if using something not standard)

```html
<!DOCTYPE html>
<html lang="en">
<head>
<meta charset="utf-8">
<title>Brightmoor Lane Inc – Business Card</title>
<link rel="stylesheet" href="https://fonts.googleapis.com/css2?family=Questrial&display=swap">
<style>
  :root {
    --bg: #2b2b2d;
    --card: #ffffff;
    --army: #556b2f;
    --red: #c62828;
    --black: #1c1c1c;
    --ink: #2a2a2a;
    --white: #ffffff;
  }
  * { margin: 0; padding: 0; box-sizing: border-box; }
  html, body { width: 1200px; height: 880px; overflow: hidden; background: var(--bg); }
  body { position: relative; font-family: "Questrial", "Century Gothic", sans-serif; }

  .card {
    position: absolute;
    width: 520px; height: 298px;
    background: var(--card);
    border-radius: 18px;
    overflow: hidden;
  }
  .card--front { left: 70px; top: 90px; }
  .card--back  { left: 610px; top: 482px; }
  .card__bands { position: absolute; inset: 0; }

  .brand { position: absolute; color: var(--army); white-space: nowrap; }
  .brand__mark {
    display: inline-block; width: 14px; height: 14px;
    background: var(--red); margin-right: 8px; vertical-align: 4px;
  }
  .card--front .brand { left: 0; right: 0; top: 62px; text-align: center; font-size: 40px; }
  .promise {
    position: absolute; left: 70px; right: 70px; top: 122px;
    text-align: center; color: var(--ink); font-size: 15px; line-height: 1.45;
  }
  .website {
    position: absolute; left: 0; right: 0; top: 236px;
    text-align: center; color: var(--white); font-size: 15px; letter-spacing: 3px;
  }

  .card--back .brand { left: 40px; top: 74px; font-size: 34px; }
  .person { position: absolute; left: 40px; top: 176px; color: var(--white); }
  .person__name { font-size: 21px; line-height: 1; }
  .person__title { font-size: 13px; margin-top: 4px; }

  .contact { position: absolute; left: 40px; top: 226px; list-style: none; color: var(--white); font-size: 13px; }
  .contact li { display: flex; align-items: center; gap: 8px; height: 20px; }
  .contact svg { width: 15px; height: 15px; flex: none; }

  .address {
    position: absolute; right: 28px; top: 158px; text-align: right;
    color: var(--white); font-size: 13px; line-height: 1.35; font-style: normal;
  }
</style>
</head>
<body>

<section class="card card--front" aria-label="Card front">
  <svg class="card__bands" viewBox="0 0 520 298" aria-hidden="true">
    <path fill="var(--red)" d="M0,246 L80,246 C110,246 110,206 150,206 L420,206 C450,206 455,176 485,176 L520,176 L520,298 L0,298 Z"/>
    <path fill="var(--black)" d="M0,270 L70,270 C105,270 105,218 150,218 L420,218 C450,218 455,190 490,190 L520,190 L520,298 L0,298 Z"/>
  </svg>
  <div class="brand"><span class="brand__mark"></span>Brightmoor Lane Inc</div>
  <p class="promise">I equip results-oriented business leaders to turn their people problems into profits in six months or less.</p>
  <p class="website">www.brightmoorlane.com</p>
</section>

<section class="card card--back" aria-label="Card back">
  <svg class="card__bands" viewBox="0 0 520 298" aria-hidden="true">
    <path fill="var(--army)" d="M0,168 L255,168 C280,168 282,132 310,132 L520,132 L520,298 L0,298 Z"/>
    <path fill="var(--black)" d="M0,218 L265,218 C292,218 292,148 322,148 L520,148 L520,298 L0,298 Z"/>
  </svg>
  <div class="brand"><span class="brand__mark"></span>Brightmoor Lane Inc</div>
  <div class="person">
    <p class="person__name">Dana Whitfield</p>
    <p class="person__title">Chief Performance Strategist</p>
  </div>
  <ul class="contact">
    <li>
      <svg viewBox="0 0 16 16"><circle cx="8" cy="8" r="7.2" fill="none" stroke="#fff" stroke-width="1.2"/><path d="M5 6.5c0-1 1.5-1.6 3-1.6s3 .6 3 1.6l-1 .6-.6-1H6.6l-.6 1zM5.6 8h4.8l.6 3H5z" fill="#fff"/></svg>
      555-014-2236
    </li>
    <li>
      <svg viewBox="0 0 16 16"><circle cx="8" cy="8" r="7.2" fill="none" stroke="#fff" stroke-width="1.2"/><rect x="5.6" y="3.8" width="4.8" height="8.4" rx="1" fill="none" stroke="#fff" stroke-width="1.1"/></svg>
      555-019-4871
    </li>
    <li>
      <svg viewBox="0 0 16 16"><circle cx="8" cy="8" r="7.2" fill="none" stroke="#fff" stroke-width="1.2"/><rect x="4.2" y="5.4" width="7.6" height="5.2" fill="#fff"/><path d="M4.2 5.4L8 8.4l3.8-3" fill="none" stroke="var(--black)" stroke-width="1"/></svg>
      danaw@brightmoorlane.com
    </li>
  </ul>
  <address class="address">
    Brightmoor Lane, Inc.<br>
    1820 Orchard Road #410<br>
    Fairview, MI 48000
  </address>
</section>

</body>
</html>
```